Website Design for a DJ Entertainment and Productions Comany

We are a full service DJ Entertainment and Productions company looking to have a strong presence in our local market and need a phenomenal website design to drive clients to the site but then also keep them there. We cater to all types of different events varying from weddings to proms to corporate events, birthdays, bar mitzvah's and so on and so on. We also do full lighting for any type of event and we also offer a photobooth service for various events. The best way to get an idea of the services that we offer is to visit http://www.velvarmusicworks.com/index.html This site is NOT our own but only linked as an example of what we do and will give you an overall overview of what we offer.
We are looking for pure creativity as there are multiple facets to our company and the services we offer. On the one hand we can provide a night club party atmosphere for Proms or dances but on the other hand we also provide professional full service emcee/DJ for weddings and formal events. The key for this site would be to have the pages for each category match the look and feel of the actual service provided, ie the Wedding page will look more refined and professional vs the Party DJ page. Each page needs to fit the overall feel of the Company and Logo though. Here is a list of pages that we would need to have on the final site.
HOME PAGE
PROFESSINAL DJS- This will have info. and pricing of our DJ services for everything but weddings. Should have pics and videos somewhere on this page.
WEDDINGS- All wedding package pricing and info. This page should look more elegant, formal and high class compared to the other pages.
PHOTOBOOTH-Page with info, pricing on photobooth see http://www.glimmerboxkiosk.com/
LIGHTING DESIGN-Info on our lighting services along with pricing
CORPORATE EVENTS-Info on services and pricing for corporate events. This page should seem more professional centered towards business clientele.
CLIENT LOGIN-Page for existing clients to logon to update info and fill out information.
CONNECT WITH US- Social Media links.
Our logo was submitted through Pixel Forum but I am open to suggestions on revisions if you feel the need to change it. Color is also not set in stone.
Updates
I have increased my budget $200 more. Please submit your designs for review, deadline is approaching quickly. Also see brief for revisions.
Thank you.
Target Market(s)
Broad Range but usually Under 40
Industry/Entity Type
Night Club
Look and feel

```html
<!DOCTYPE html>
<html lang="en">
<head>
<meta charset="utf-8">
<title>NOVA Entertainment &amp; Productions</title>
<link href="https://fonts.googleapis.com/css2?family=Open+Sans:wght@400;600;700&family=Arimo:wght@400;700&family=Roboto:wght@300;400&family=Playfair+Display:ital,wght@1,700&display=swap" rel="stylesheet">
<style>
:root{
  --red:#d9262b;
  --red-dark:#a8161b;
  --ink:#333;
  --muted:#888;
  --band:#e6e6e6;
  --gray:#d3d3d3;
  --btn-dark:#3b3b3b;
  --beige:#b89a8e;
}
*{margin:0;padding:0;box-sizing:border-box}
html,body{width:943px;height:1200px;overflow:hidden;background:#fff}
body{position:relative;font-family:"Arimo",Arial,sans-serif;color:var(--ink)}
.abs{position:absolute}

/* navigation */
.nav{position:absolute;top:0;left:342px;display:flex;gap:4px;z-index:3}
.nav a{display:block;height:30px;line-height:26px;padding:0 6px;font:600 11px "Open Sans",sans-serif;color:#333;text-decoration:none;background:linear-gradient(#e8e8e8,#c9c9c9);border-radius:0 0 6px 6px}
.nav a.current{background:linear-gradient(#444,#1d1d1d);color:#fff;padding:0 11px}

/* brand */
.brand{top:20px;left:51px;display:flex;align-items:center;gap:12px;z-index:3}
.brand-mark{width:70px;height:70px;border-radius:50%;background:var(--red)}
.brand-name{font:700 44px/1 "Open Sans",sans-serif;color:var(--red);letter-spacing:2px}
.brand-sub{font:600 10px "Open Sans",sans-serif;color:var(--red);margin-top:3px}

/* hero */
.hero-bg{top:0;left:0}
.hero-title{top:151px;left:85px;width:420px;font:700 16px/21px "Open Sans",sans-serif;color:#fff;text-shadow:0 1px 2px rgba(0,0,0,.4)}
.hero-list{top:200px;left:85px;list-style:none;font:400 14.5px/24px "Open Sans",sans-serif;color:#fff}
.hero-list li::before{content:"»";font-weight:700;margin-right:10px}
.hero-art{top:90px;left:530px;width:340px;height:275px;border-radius:40%;background:radial-gradient(ellipse at 55% 55%,rgba(255,255,255,.35) 0%,rgba(255,255,255,.12) 45%,rgba(255,255,255,0) 70%)}
.arrow{width:46px;height:46px;border-radius:50%;border:3px solid #8e1014;top:201px;display:flex;align-items:center;justify-content:center}
.dots{top:350px;left:57px;display:flex;gap:12px}
.dots span{width:14px;height:14px;border-radius:50%;background:#999}
.dots span.on{background:#333;box-shadow:0 0 0 2px #aaa}

/* intro band */
.intro{top:383px;left:0;width:943px;height:71px;background:var(--band);border-bottom:1px solid #ccc}
.intro p{position:absolute;left:51px;top:17px;width:630px;font:400 13px/22px "Open Sans",sans-serif;color:#444}
.book{position:absolute;left:692px;top:14px;width:191px;height:44px;border-radius:5px;background:linear-gradient(#4a4a4a,#222);color:#fff;font:700 18px/44px "Open Sans",sans-serif;text-align:center;letter-spacing:.5px}

/* gallery */
.shot{top:468px;width:186px;height:142px;background:#333;padding:5px;box-shadow:0 8px 6px -6px rgba(0,0,0,.35)}
.shot div{width:100%;height:100%;border:1px solid #fff}
.chev{top:510px;font:700 56px/1 "Open Sans",sans-serif;color:#333}

/* columns */
.col-title{top:642px;font:700 18px "Open Sans",sans-serif;color:#444;letter-spacing:1px}
.rule-v{top:660px;width:1px;height:170px;background:#e2e2e2}
.news{left:51px;width:250px;display:flex;gap:10px}
.thumb{width:70px;height:52px;flex:none;border:2px solid #999;background:linear-gradient(135deg,#3a1c5c,#c243a8 50%,#1b1030)}
.news h4{font:700 11px Arimo,sans-serif;margin-bottom:4px}
.news p{font:400 11px/17px Arimo,sans-serif;color:#444}
.dotted{height:0;border-top:1px dotted #aaa}
.dest-img{top:676px;left:321px;width:253px;height:81px;border:2px solid #555;background:linear-gradient(90deg,#6d0f3a,#e04d8c 40%,#f5d0e0 55%,#5a1632)}
.dest-text{top:766px;left:323px;width:253px;font:400 10.5px/15.5px Arimo,sans-serif;color:#444;text-align:justify}
.tracks{top:674px;left:614px;width:275px;list-style:none}
.tracks li{display:flex;align-items:center;height:22.3px;font:400 10.5px Arimo,sans-serif;color:#222}
.tracks .disc{width:11px;height:11px;border-radius:50%;background:#222;margin-right:7px;border:2px solid #bbb}
.tracks .disc.play{background:#ddd;border-color:#999}
.tracks em{font-style:normal;color:#999}
.tracks .stars{margin-left:auto;font-size:10px;letter-spacing:1px;color:#111}
.tracks .stars i{font-style:normal;color:#bbb}
.btn{top:841px;width:66px;height:21px;border-radius:3px;color:#fff;font:700 10px/21px Arimo,sans-serif;text-align:center}
.btn.red{background:linear-gradient(#e0353a,#b01b20)}
.btn.dark{background:linear-gradient(#555,#2a2a2a)}

/* promos */
.wed{top:896px;left:51px;width:222px;height:141px;border-radius:4px;background:linear-gradient(135deg,#e33237,#b4161b)}
.wed-art{position:absolute;left:4px;top:10px;width:80px;height:95px;background:radial-gradient(circle,#e8e8e8,#c0c0c0 50%,transparent 70%)}
.wed h3{position:absolute;left:90px;top:14px;font:700 italic 20px/26px "Playfair Display",serif;color:#fff}
.wed .btn{top:112px;left:143px;width:67px;border:1px solid #fff;box-shadow:0 0 0 1px #333}
.clients{top:896px;left:284px;width:605px;height:141px;border:1px solid #ddd;border-radius:4px;background:linear-gradient(#fafafa,#e2e2e2)}
.clients h3{position:absolute;left:12px;top:6px;font:700 italic 21px "Playfair Display",serif;color:#666}
.client-row{position:absolute;left:10px;top:58px;width:585px;display:flex;justify-content:space-between;align-items:center}
.client-row span{display:flex;align-items:center;gap:5px;font:600 12px "Open Sans",sans-serif;color:#555}
.client-row b{width:10px;height:10px;border-radius:50%;background:#999;display:inline-block}
.clients .more{position:absolute;right:12px;top:119px;font:italic 11px Arimo,sans-serif;color:#c4161c}

/* footer */
.foot{left:0;width:943px;text-align:center;font:300 11.5px "Roboto",sans-serif;color:#555;letter-spacing:.5px}
.foot-links{top:1058px}
.foot-links a{color:#555;text-decoration:none}
.crowd{top:1097px;left:0;width:943px;height:103px;background:linear-gradient(rgba(184,154,142,0),rgba(184,154,142,.85) 55%,var(--beige))}
</style>
</head>
<body>

<svg class="abs hero-bg" width="943" height="390" viewBox="0 0 943 390">
  <defs>
    <linearGradient id="heroRed" x1="0" y1="0" x2="1" y2="1">
      <stop offset="0" stop-color="#c81f24"/>
      <stop offset=".5" stop-color="#e02a30"/>
      <stop offset="1" stop-color="#c21c21"/>
    </linearGradient>
  </defs>
  <polygon points="0,383 943,383 943,390 0,390" fill="var(--gray)"/>
  <polygon points="0,326 943,383 0,383" fill="var(--gray)"/>
  <polygon points="0,140 943,43 943,383 0,326" fill="url(#heroRed)"/>
  <polygon points="0,134 943,37 943,43 0,140" fill="#eee"/>
</svg>

<nav class="nav">
  <a class="current" href="#">Home page</a>
  <a href="#">Weddings-all</a>
  <a href="#">Photobooth</a>
  <a href="#">Lighting Design</a>
  <a href="#">Corporate Event</a>
  <a href="#">Client login</a>
  <a href="#">Connect us</a>
</nav>

<div class="abs brand">
  <div class="brand-mark"></div>
  <div>
    <div class="brand-name">NOVA</div>
    <div class="brand-sub">ENTERTAINMENT &amp; PRODUCTIONS</div>
  </div>
</div>

<div class="abs hero-art" role="img" aria-label="Illustration of a DJ at turntables with a dancing figure and a script headline"></div>
<h1 class="abs hero-title">Lorem Ipsum is simply dummy text of the printing and typesetting industry.</h1>
<ul class="abs hero-list">
  <li>No cost to set up your online store</li>
  <li>Get paid quarterly via CoinPost</li>
  <li>Retain an un-heard of 80%</li>
  <li>Free widgets for your SpaceHub or FriendBook</li>
  <li>Make Apricado Jam!</li>
</ul>
<div class="abs arrow" style="left:31px"><svg width="18" height="22"><polygon points="16,1 16,21 2,11" fill="#8e1014"/></svg></div>
<div class="abs arrow" style="left:863px"><svg width="18" height="22"><polygon points="2,1 2,21 16,11" fill="#8e1014"/></svg></div>
<div class="abs dots"><span></span><span class="on"></span><span></span><span></span><span></span><span></span></div>

<section class="abs intro">
  <p>Our modern photo boots feature a unique design and use the latest digital cameras and professional printing tecnology to provide a professional and exciting experience that will be the hit of your envent</p>
  <div class="book">Book Your Events</div>
</section>

<div class="abs chev" style="left:50px">&#10094;</div>
<div class="abs shot" style="left:84px"><div role="img" aria-label="Photo of a DJ playing to a club crowd" style="background:linear-gradient(160deg,#7a2fb8,#2a1150 60%,#111)"></div></div>
<div class="abs shot" style="left:279px"><div role="img" aria-label="Photo of a packed dance floor under stage lights" style="background:linear-gradient(170deg,#2b66c9,#0d1a3c 60%,#05070f)"></div></div>
<div class="abs shot" style="left:476px"><div role="img" aria-label="Photo of a group of party guests behind a DJ deck" style="background:linear-gradient(170deg,#e8d7c3,#b89a7e 60%,#3a3028)"></div></div>
<div class="abs shot" style="left:674px"><div role="img" aria-label="Photo of dancers in yellow club lighting" style="background:radial-gradient(circle at 55% 45%,#e8f03a,#7a8a12 45%,#1a1a05)"></div></div>
<div class="abs chev" style="left:866px">&#10095;</div>

<h2 class="abs col-title" style="left:51px">WHAT’S NEW</h2>
<h2 class="abs col-title" style="left:321px">DESTINATIONS</h2>
<h2 class="abs col-title" style="left:616px">DJ TRACKS</h2>
<div class="abs rule-v" style="left:309px"></div>
<div class="abs rule-v" style="left:597px"></div>

<div class="abs news" style="top:679px">
  <div class="thumb" role="img" aria-label="Club night photo"></div>
  <div><h4>TUE, JULY 18</h4><p>Loreterdum vitaapibus ac sue vitae ec eget telus non at lania fluonec</p></div>
</div>
<div class="abs dotted" style="top:742px;left:56px;width:245px"></div>
<div class="abs news" style="top:754px">
  <div class="thumb" role="img" aria-label="Club night photo"></div>
  <div><h4>TUE, AUG 03</h4><p>Loreterdum vitaapibus ac sue vitae ec eget telus non at lania fluonec</p></div>
</div>

<div class="abs dest-img" role="img" aria-label="Photo of a nightclub interior with pink lighting"></div>
<p class="abs dest-text">Loreterdum vitaapibus ac sue vitae ec eget telus non at lania fluonec in vel ipsum auvorpt fe lies tibulum iaculis lacinia ictum elementum velimod cquat anteorem ipsum dit conseetuer.</p>

<ul class="abs tracks">
  <li><span class="disc play"></span>PRAESENT - <em>VESTIBULUM</em><span class="stars">★★★★★</span></li>
  <li><span class="disc"></span>MOLESTIE LACUS - <em>AENEAN NONUMY</em><span class="stars">★★★<i>★★</i></span></li>
  <li><span class="disc"></span>HEIT - <em>MAURIS PHASEL LUS</em><span class="stars">★★★★★</span></li>
  <li><span class="disc"></span>PORTA - <em>FUSCE SUSCIPIT VARIUS</em><span class="stars">★★★★<i>★</i></span></li>
  <li><span class="disc"></span>MI CUMC - <em>NAUE PENATI BUS</em><span class="stars">★★★<i>★★</i></span></li>
  <li><span class="disc"></span>ET MAGNI - <em>DIS PART URIE NTMUR</em><span class="stars">★★★★<i>★</i></span></li>
  <li><span class="disc"></span>RIDICU LU - <em>MUS NULLA</em><span class="stars">★★★★<i>★</i></span></li>
</ul>

<div class="abs btn red" style="left:233px">Readmore</div>
<div class="abs btn dark" style="left:518px">Readmore</div>
<div class="abs btn dark" style="left:827px">Readmore</div>

<div class="abs dotted" style="top:879px;left:56px;width:830px"></div>

<section class="abs wed">
  <div class="wed-art" role="img" aria-label="Illustration of a guitar and a vinyl record"></div>
  <h3>weddings<br>and formal<br>events</h3>
  <div class="abs btn dark">Readmore</div>
</section>

<section class="abs clients">
  <h3>Our Client</h3>
  <div class="client-row">
    <span><b></b>Stellar Motors</span>
    <span>Brewline</span>
    <span>Peakcast</span>
    <span>Kidzone</span>
    <span>Strider</span>
    <span>Voltwell</span>
    <span>Loop Records</span>
  </div>
  <div class="more">Read more about our featured clients »</div>
</section>

<div class="abs crowd" role="img" aria-label="Silhouettes of a cheering crowd, musicians and dancers"></div>
<div class="abs foot foot-links"><a href="#">Home page</a> &nbsp;|&nbsp; <a href="#">Weddings-all</a> &nbsp;|&nbsp; <a href="#">Photobooth</a> &nbsp;|&nbsp; <a href="#">Lighting Design</a> &nbsp;|&nbsp; <a href="#">Corporate Event</a> &nbsp;|&nbsp; <a href="#">Client login</a> &nbsp;|&nbsp; <a href="#">Connect us</a></div>
<div class="abs foot" style="top:1077px">© 2011 Velvar Event Group LLC &nbsp; 800.555.0142</div>
<div class="abs foot" style="top:1096px">NOVA Entertainment &amp; Productions</div>
<div class="abs foot" style="top:1115px">E-mail | Privacy</div>

</body>
</html>
```